Showroom Quote Web Application - Prism Layout wanted

This web app is an internal application that will be used by one of our customers to build quotes and produce orders of retail items with their customers

the overall design should use the colour pallet provided and have a clean and simple interface

we'd like to go with a prism layout type of look

attached mockups are just a rough stab at some layouts to give you an example, please feel free to reach out with any questions.

Please don't get hung up on the specific pages, they were intended to provide context, we are looking for a high level design using the provided colour schemes and fonts, additional work may follow for the selected designer when it comes to specific pages or work flows.

Sorry for the short timeline, we have a tight deadline on this one.

Target Market(s)

internal application for customer

Industry/Entity Type

Retail

Other font styles liked:
• see attached doc for fonts

Requirements
Must have
• simple and clean interface
• intuitive design
Nice to have
• see attached documents for logo colour schemes and fonts
• these must be incorporated into the design

```html
<!DOCTYPE html>
<html lang="en">
<head>
<meta charset="utf-8">
<title>Plumbing Showroom Quote System – Login</title>
<link rel="stylesheet" href="https://fonts.googleapis.com/css2?family=Roboto:ital,wght@0,400;0,500;1,400&display=swap">
<style>
  :root {
    --page-bg: #eaeef2;
    --card-bg: #ffffff;
    --title-ink: #2b2b2b;
    --field-ink: #3a3a3a;
    --field-border: #d6d9dd;
    --brand-navy: #0d3578;
    --button-ink: #ffffff;
    --muted-ink: #8a8a8a;
  }
  * { box-sizing: border-box; margin: 0; padding: 0; }
  html, body {
    width: 1200px;
    height: 884px;
    overflow: hidden;
    background: var(--page-bg);
    font-family: "Roboto", Arial, sans-serif;
  }
  .login-page {
    position: relative;
    width: 1200px;
    height: 884px;
  }
  .app-title {
    position: absolute;
    top: 226px;
    left: 0;
    width: 100%;
    text-align: center;
    font-size: 28px;
    font-weight: 500;
    color: var(--title-ink);
    letter-spacing: 0.1px;
  }
  .login-card {
    position: absolute;
    top: 300px;
    left: 297px;
    width: 606px;
    height: 307px;
    background: var(--card-bg);
    box-shadow: 0 1px 4px rgba(0, 0, 0, 0.12);
  }
  .field {
    position: absolute;
    left: 43px;
    width: 521px;
    height: 58px;
    border: 1px solid var(--field-border);
    background: var(--card-bg);
    padding: 0 20px;
    font-family: inherit;
    font-size: 22px;
    color: var(--field-ink);
    outline: none;
  }
  .field::placeholder { color: var(--field-ink); opacity: 1; }
  .field-username { top: 47px; }
  .field-password { top: 117px; }
  .login-button {
    position: absolute;
    top: 199px;
    left: 43px;
    width: 171px;
    height: 59px;
    border: none;
    background: var(--brand-navy);
    color: var(--button-ink);
    font-family: inherit;
    font-size: 21px;
    font-weight: 400;
    letter-spacing: 0.4px;
    box-shadow: 0 2px 4px rgba(0, 0, 0, 0.25);
    cursor: pointer;
  }
  .forgot-link {
    position: absolute;
    top: 214px;
    right: 42px;
    font-size: 20px;
    font-style: italic;
    color: var(--muted-ink);
    text-decoration: none;
  }
</style>
</head>
<body>
  <main class="login-page">
    <h1 class="app-title">Plumbing Showroom Quote System (PSQS)</h1>
    <form class="login-card">
      <input class="field field-username" type="text" placeholder="Username" aria-label="Username">
      <input class="field field-password" type="password" placeholder="Password" aria-label="Password">
      <button class="login-button" type="button">LOGIN</button>
      <a class="forgot-link" href="#">Forgot password?</a>
    </form>
  </main>
</body>
</html>
```